Junior tennis development pathway graphic

The National Racquet Guild Assn.(NRGA) and the Global Court Sports Union (GCSU)
recommend (read demand) that all junior tennis programs now be ran using a progressive format of 4 different colored balls, different court sizes and scoring systems for various ages. We want to create a graphic for our juniors page on our web site that will show parents in a VERY EASY to understand way how their kids will progress through the various stages of tennis. The page is being built using Bootstrap and we plan to use jQuerry Hotspot to give detailed information over certain areas of the graphic. This specific information will be Dbase driven with class names,and specific class info. - The design does not need to show this, I just though it might be helpful to know
Updates

There are 2 other sites that will be helpful in understanding this project:

The first is www.smallcourtstarters.example and the second is my junior page on my current website
www.pinecrestracquetclub.example/juniora.cfm

I added a new file named jr pathway 2

This is an idea i had for the project - needs to be completed and given some sizzle

Target Market(s)

Parents of children ages 3-16

Industry/Entity Type

Progressive

Requirements
Must have
• Vector format
800x800 pixels max
EASY TO UNDERSTAND
Use of some or all of the key words and phrases in the uploaded file "keywords"
Should not have
• I do not want it to look like every other development graphic already out there.
To see what is currently being used image search
"tennis pathway" or "junior tennis pathway"

"pathway and" juniorspathway" in the uploaded files section are 2 ideas of VERY bad attempts

```html
<!DOCTYPE html>
<html lang="en">
<head>
<meta charset="utf-8">
<title>4 Colors One Game – Junior Tennis Pathway</title>
<link rel="stylesheet" href="https://fonts.googleapis.com/css2?family=Montserrat:wght@400;600;700;800&display=swap">
<style>
  :root {
    --red-top: #e8313a;
    --red-bottom: #d63a2c;
    --orange-top: #f06c40;
    --orange-bottom: #e48a4c;
    --green-top: #8aab44;
    --green-bottom: #7a9431;
    --yellow-top: #f6ee4a;
    --yellow-bottom: #e8df6a;
    --band-fill: rgba(30, 10, 0, 0.62);
    --band-line: rgba(255, 238, 215, 0.72);
    --band-label: rgba(255, 232, 205, 0.72);
    --white: #ffffff;
    --program-title: #f06a2a;
    --program-text: #6a5a3a;
    --ball-red: #ec2027;
    --ball-orange: #f15a29;
    --ball-green: #7cac3a;
    --ball-yellow: #eeea2a;
    --ball-seam: #d9e64a;
  }
  html, body {
    margin: 0;
    padding: 0;
    width: 1200px;
    height: 1200px;
    overflow: hidden;
  }
  body { font-family: "Montserrat", sans-serif; }
  .pathway {
    position: relative;
    width: 1200px;
    height: 1200px;
    overflow: hidden;
  }
  .stage-column {
    position: absolute;
    top: 0;
    width: 300px;
    height: 1200px;
  }
  .stage-red    { left: 0;   background: linear-gradient(var(--red-top), var(--red-bottom)); }
  .stage-orange { left: 300px; background: linear-gradient(var(--orange-top), var(--orange-bottom)); }
  .stage-green  { left: 600px; background: linear-gradient(var(--green-top), var(--green-bottom)); }
  .stage-yellow { left: 900px; background: linear-gradient(var(--yellow-top), var(--yellow-bottom)); }

  .headline-number {
    position: absolute;
    left: 70px;
    top: -38px;
    font-size: 350px;
    font-weight: 800;
    line-height: 1;
    color: var(--white);
    letter-spacing: -10px;
  }
  .headline-colors {
    position: absolute;
    left: 306px;
    top: 26px;
    font-size: 150px;
    font-weight: 800;
    line-height: 1;
    color: var(--white);
    letter-spacing: -3px;
  }
  .headline-game {
    position: absolute;
    left: 314px;
    top: 160px;
    font-size: 105px;
    font-weight: 800;
    line-height: 1;
    color: var(--white);
    letter-spacing: -2px;
  }
  .tagline {
    position: absolute;
    left: 320px;
    top: 270px;
    font-size: 18.5px;
    font-weight: 700;
    color: var(--white);
  }

  .player-art {
    position: absolute;
    border-radius: 40px;
  }
  .player-red    { left: 72px;  top: 292px; width: 222px; height: 312px; background: linear-gradient(#ef6a3a, #b42a26); opacity: .55; }
  .player-orange { left: 328px; top: 316px; width: 230px; height: 376px; background: linear-gradient(#3f6fc8, #f6d9c5); opacity: .5; }
  .player-green  { left: 580px; top: 372px; width: 255px; height: 392px; background: linear-gradient(#e6e6e6, #2f8a3c); opacity: .5; }
  .player-yellow { left: 912px; top: 480px; width: 276px; height: 456px; background: linear-gradient(#f06aa2, #eeeeee); opacity: .55; }

  .age-label {
    position: absolute;
    font-size: 18.5px;
    font-weight: 700;
    color: var(--white);
  }
  .age-red    { left: 98px;  top: 630px; }
  .age-orange { left: 467px; top: 630px; }
  .age-green  { left: 788px; top: 648px; }
  .age-yellow { left: 1043px; top: 800px; }

  .program-note {
    position: absolute;
    left: 956px;
    top: 266px;
    font-size: 19.5px;
    line-height: 25px;
    color: var(--program-text);
  }
  .program-note h2 {
    margin: 0;
    font-size: 19.5px;
    font-weight: 600;
    color: var(--program-title);
  }
  .program-note ul { margin: 0; padding: 0; list-style: none; }

  .band-frames {
    position: absolute;
    left: 0;
    top: 0;
  }
  .band-fill { fill: var(--band-fill); }
  .band-outline { fill: none; stroke: var(--band-line); stroke-width: 3; }

  .band-label {
    position: absolute;
    font-size: 36px;
    font-weight: 700;
    color: var(--band-label);
    line-height: 1;
    letter-spacing: 1px;
    transform: translateX(-50%);
  }
  .label-learn   { left: 447px; top: 742px; }
  .label-play    { left: 447px; top: 888px; }
  .label-compete { left: 711px; top: 1031px; }

  .level {
    position: absolute;
    display: flex;
    align-items: center;
    gap: 10px;
    font-size: 24px;
    font-weight: 700;
    line-height: 1.25;
    color: var(--white);
  }
  .level svg { width: 56px; height: 56px; flex: none; }
  .ball-seam { fill: none; stroke: var(--white); stroke-width: 2.5; }
</style>
</head>
<body>
<main class="pathway">
  <div class="stage-column stage-red"></div>
  <div class="stage-column stage-orange"></div>
  <div class="stage-column stage-green"></div>
  <div class="stage-column stage-yellow"></div>

  <h1 class="headline">
    <span class="headline-number">4</span>
    <span class="headline-colors">COLORS</span>
    <span class="headline-game">ONE GAME</span>
  </h1>
  <p class="tagline">YOUR CHILD’S PATH TO SUCCESS AT EVERY LEVEL (AGE)</p>

  <div class="player-art player-red" role="img" aria-label="Illustration of a young child hitting a backhand, red stage"></div>
  <div class="player-art player-orange" role="img" aria-label="Illustration of a girl preparing a forehand, orange stage"></div>
  <div class="player-art player-green" role="img" aria-label="Illustration of a boy in a cap hitting a backhand, green stage"></div>
  <div class="player-art player-yellow" role="img" aria-label="Illustration of a teenage girl hitting a forehand, yellow stage"></div>

  <span class="age-label age-red">Age: 5-8</span>
  <span class="age-label age-orange">Age: 7-10</span>
  <span class="age-label age-green">Age: 10-14</span>
  <span class="age-label age-yellow">Age: 10-18</span>

  <section class="program-note">
    <h2>What is a program?</h2>
    <ul>
      <li>-teaching/coaching</li>
      <li>-training/practicing</li>
      <li>-competition</li>
      <li>-play</li>
      <li>-social</li>
    </ul>
  </section>

  <svg class="band-frames" width="1200" height="1200" viewBox="0 0 1200 1200" aria-hidden="true">
    <rect class="band-fill" x="13" y="770" width="879" height="89"/>
    <path class="band-outline" d="M527 770 H892 V859 H13 V770 H367"/>
    <rect class="band-fill" x="13" y="916" width="879" height="88"/>
    <path class="band-outline" d="M515 916 H892 V1004 H13 V916 H380"/>
    <path class="band-fill" d="M311 1062 H858 L903 1026 H1187 V1173 H903 L858 1145 H311 Z"/>
    <path class="band-outline" d="M818 1062 H858 L903 1026 H1187 V1173 H903 L858 1145 H311 V1062 H604"/>
  </svg>

  <span class="band-label label-learn">LEARN</span>
  <span class="band-label label-play">PLAY</span>
  <span class="band-label label-compete">COMPETE</span>

  <!-- Learn -->
  <div class="level" style="left:72px; top:790px;">
    <svg viewBox="0 0 56 56"><circle cx="28" cy="28" r="25" fill="var(--ball-red)" stroke="var(--white)" stroke-width="3"/><path class="ball-seam" d="M10 12 Q30 22 16 48"/></svg>Red 1</div>
  <div class="level" style="left:349px; top:790px;">
    <svg viewBox="0 0 56 56"><circle cx="28" cy="28" r="25" fill="var(--ball-orange)" stroke="var(--white)" stroke-width="3"/><path class="ball-seam" d="M10 12 Q30 22 16 48"/></svg>Orange 1</div>
  <div class="level" style="left:644px; top:790px;">
    <svg viewBox="0 0 56 56"><circle cx="28" cy="28" r="25" fill="var(--ball-green)" stroke="var(--white)" stroke-width="3"/><path class="ball-seam" d="M10 12 Q30 22 16 48"/></svg>Green 1</div>

  <!-- Play -->
  <div class="level" style="left:72px; top:932px;">
    <svg viewBox="0 0 56 56"><circle cx="28" cy="28" r="25" fill="var(--ball-red)" stroke="var(--white)" stroke-width="3"/><path class="ball-seam" d="M10 12 Q30 22 16 48"/></svg>Red 2</div>
  <div class="level" style="left:349px; top:932px;">
    <svg viewBox="0 0 56 56"><circle cx="28" cy="28" r="25" fill="var(--ball-orange)" stroke="var(--white)" stroke-width="3"/><path class="ball-seam" d="M10 12 Q30 22 16 48"/></svg>Orange 2</div>
  <div class="level" style="left:644px; top:932px;">
    <svg viewBox="0 0 56 56"><circle cx="28" cy="28" r="25" fill="var(--ball-green)" stroke="var(--white)" stroke-width="3"/><path class="ball-seam" d="M10 12 Q30 22 16 48"/></svg><span>Junior Tennis<br>League</span></div>

  <!-- Compete -->
  <div class="level" style="left:349px; top:1077px;">
    <svg viewBox="0 0 56 56"><circle cx="28" cy="28" r="25" fill="var(--ball-orange)" stroke="var(--white)" stroke-width="3"/><path class="ball-seam" d="M10 12 Q30 22 16 48"/></svg>JTS Orange</div>
  <div class="level" style="left:644px; top:1077px;">
    <svg viewBox="0 0 56 56"><circle cx="28" cy="28" r="25" fill="var(--ball-green)" stroke="var(--white)" stroke-width="3"/><path class="ball-seam" d="M10 12 Q30 22 16 48"/></svg>JTS Green</div>
  <div class="level" style="left:939px; top:1036px;">
    <svg viewBox="0 0 56 56"><circle cx="28" cy="28" r="25" fill="var(--ball-yellow)" stroke="var(--white)" stroke-width="3"/><path class="ball-seam" d="M10 12 Q30 22 16 48"/></svg>JTS Yellow</div>
  <div class="level" style="left:939px; top:1103px;">
    <svg viewBox="0 0 56 56"><circle cx="28" cy="28" r="25" fill="var(--ball-yellow)" stroke="var(--white)" stroke-width="3"/><path class="ball-seam" d="M10 12 Q30 22 16 48"/></svg><span>High school<br>team</span></div>
</main>
</body>
</html>
```